Single brochure for international companies in the financial sector

We need to update a brochure 4 pages presenting our company. We are a financial engineering company. The final design must provide financial security, service and trust. you will find the current brochure copy. Our color code is Orange (RGB 235/100/68), Black, White and Gray. photos show the visual of the site, but it is not mandatory to keep them.

Target Market(s)

wealth management professionals

Industry/Entity Type

Finance

Requirements
Must have
• Logo Velbrook Capital all text in the document color Orange Velbrook (RGB 235/100/68)
Nice to have
• Vista Font
Should not have
• images / pictures of people

```html
<!DOCTYPE html>
<html lang="en">
<head>
<meta charset="utf-8">
<title>Velbrook Capital – The Company</title>
<link href="https://fonts.googleapis.com/css2?family=Questrial&display=swap" rel="stylesheet">
<style>
  :root {
    --orange: #eb6444;
    --orange-light: #f38a6c;
    --ink: #1d1d1d;
    --body: #4a4a4a;
    --rule: #6b6b6b;
    --paper: #ffffff;
    --stone-dark: #6f6a6a;
    --stone-light: #c9c5c4;
  }
  * { margin: 0; padding: 0; box-sizing: border-box; }
  html, body { width: 785px; height: 1200px; overflow: hidden; background: var(--paper); }
  body { font-family: "Questrial", "Century Gothic", sans-serif; color: var(--body); }

  .page { position: relative; width: 785px; height: 1200px; background: var(--paper); }

  .hero {
    position: absolute; left: 0; top: 0; width: 785px; height: 262px;
    background: linear-gradient(160deg, var(--stone-light) 0%, #a29d9c 45%, var(--stone-dark) 100%);
    border-bottom: 2px solid var(--orange);
  }
  .hero-title {
    position: absolute; left: 0; top: 196px; width: 394px; height: 66px;
    background: linear-gradient(90deg, var(--orange) 0%, var(--orange-light) 70%, var(--orange) 100%);
    color: var(--paper); font-size: 36px; letter-spacing: 0.5px;
    padding-left: 58px; line-height: 66px;
  }

  .intro { position: absolute; left: 58px; width: 358px; }
  .section-title { font-size: 23px; color: var(--ink); font-weight: 400; }
  .section-text {
    font-size: 15px; line-height: 31px; color: var(--body);
    text-align: justify; letter-spacing: 0.3px; margin-top: 14px;
  }
  .section-text + .section-text { margin-top: 8px; }

  .pull-quote { position: absolute; left: 456px; top: 340px; width: 300px; color: var(--orange); }
  .quote-mark { position: absolute; left: 0; top: 0; font-size: 48px; line-height: 48px; }
  .quote-text {
    margin-left: 44px; font-size: 24px; line-height: 46px; letter-spacing: 1.6px;
  }
  .quote-text + .quote-text { margin-top: 46px; }

  .footer { position: absolute; left: 0; top: 1122px; width: 785px; height: 24px; }
  .footer-rule { position: absolute; top: 12px; height: 1px; background: var(--rule); }
  .footer-rule.left { left: 0; width: 230px; }
  .footer-rule.right { left: 554px; width: 231px; }
  .footer-brand {
    position: absolute; left: 230px; width: 324px; text-align: center;
    color: var(--orange); font-size: 16px; letter-spacing: 5px; line-height: 24px;
  }
</style>
</head>
<body>
<main class="page">
  <header class="hero" role="img" aria-label="Photograph of a granite cobblestone wall with steel rails in grey tones"></header>
  <h1 class="hero-title">THE COMPANY</h1>

  <section class="intro" style="top: 340px;">
    <h2 class="section-title">About Us</h2>
    <p class="section-text">Velbrook Capital is a financial engineering company. It is fully independent from any bank or any other company.</p>
  </section>

  <section class="intro" style="top: 532px;">
    <h2 class="section-title">Our Clients</h2>
    <p class="section-text">Our clients are financial professionals such as asset managers, institutionnals, corporates, private banks, wealth managers and family offices.</p>
    <p class="section-text">Our purpose is to make their work easier, every day.</p>
  </section>

  <section class="intro" style="top: 833px;">
    <h2 class="section-title">What We Do</h2>
    <p class="section-text">We provide them with investment solutions designed to improve their portfolios performance.</p>
    <p class="section-text">Simple as that.</p>
  </section>

  <aside class="pull-quote">
    <span class="quote-mark">&ldquo;</span>
    <p class="quote-text">Our Clients must deliver performance on their portfolios on a regular basis.</p>
    <p class="quote-text">We help them deliver everyday.</p>
  </aside>

  <footer class="footer">
    <span class="footer-rule left"></span>
    <span class="footer-brand">VELBROOK CAPITAL</span>
    <span class="footer-rule right"></span>
  </footer>
</main>
</body>
</html>
```